Flyer / Small Safety "Poster" (A4 or 8.5x11" paper)

We're looking to create a series of safety signs for woodworkers to print on home printers using standard sized paper (A4 or 8.5x11" depending on where they are), or possibly to have printed on 17x22" paper.
Currently we want only the first one, but keep in mind that all should work together.
They need: Simple graphic. Bold Text. Company logo. Use company colors (orange, black, white.)
To begin, we will start with a single sign for hearing protection. Graphic or clip art to portray either ear plugs or ear-muff design. Text to say, "Hearing Protection is a Sound Investment."

Target Market(s)

USA Woodworkers & CNC Machinists - Male, 20-65 years old

Font styles to use
Sans Serif

Colors
f37122

Requirements
Must have
• Client logo
Nice to have
• Use client colors of black, white, & orange

```html
<!DOCTYPE html>
<html lang="en">
<head>
<meta charset="utf-8">
<title>Hearing Protection Safety Sign</title>
<link href="https://fonts.googleapis.com/css2?family=Montserrat:ital,wght@0,800;0,900;1,500&display=swap" rel="stylesheet">
<style>
  :root{
    --orange:#f37122;
    --black:#000000;
    --white:#ffffff;
  }
  html,body{margin:0;padding:0;overflow:hidden;background:var(--white);}
  .sign{
    position:relative;width:936px;height:1200px;overflow:hidden;
    background:var(--white);font-family:"Montserrat",Arial,sans-serif;
  }
  .hazard-band{
    position:absolute;height:24px;
    background:repeating-linear-gradient(-60deg,var(--orange) 0 14px,var(--black) 14px 28px);
  }
  .hazard-band--top{top:0;left:0;right:0;}
  .hazard-band--bottom{bottom:0;left:362px;right:0;height:30px;}
  .headline{position:absolute;top:48px;left:0;right:0;text-align:center;margin:0;}
  .headline__main{
    display:block;color:var(--orange);font-weight:900;
    font-size:118px;line-height:106px;letter-spacing:-1px;
  }
  .headline__sub{
    display:block;color:var(--black);font-weight:900;
    font-size:51px;line-height:58px;margin-top:8px;letter-spacing:1px;
  }
  .photo-area{position:absolute;left:0;top:380px;width:700px;height:820px;}
  .icon-stack{position:absolute;left:739px;top:408px;width:146px;}
  .icon{display:block;width:146px;height:146px;margin-bottom:20px;}
  .brand{
    position:absolute;left:530px;top:962px;width:340px;text-align:center;
  }
  .brand__name{
    display:flex;align-items:center;justify-content:center;gap:12px;
    font-weight:900;font-size:42px;line-height:50px;color:var(--black);
    letter-spacing:2px;margin:0;
  }
  .brand__mark{width:22px;height:22px;background:var(--black);flex:none;}
  .brand__name span{display:block;text-align:left;}
  .brand__tagline{
    margin:18px 0 0;font-style:italic;font-weight:500;font-size:14px;color:var(--black);
  }
  .brand__url{margin:22px 0 0;font-weight:800;font-size:19px;color:var(--black);}
</style>
</head>
<body>
<main class="sign">
  <div class="hazard-band hazard-band--top"></div>

  <h1 class="headline">
    <span class="headline__main">HEARING<br>PROTECTION</span>
    <span class="headline__sub">IS A SOUND INVESTMENT</span>
  </h1>

  <svg class="photo-area" viewBox="0 0 700 820" role="img" aria-label="Photo of a smiling worker wearing an orange hard hat, yellow safety glasses and orange earmuffs">
    <defs>
      <linearGradient id="photoTone" x1="0" y1="0" x2="0.7" y2="1">
        <stop offset="0" stop-color="#f7a35c"/>
        <stop offset="0.35" stop-color="var(--orange)"/>
        <stop offset="0.6" stop-color="#ecc2ad"/>
        <stop offset="0.85" stop-color="#3a6bd0"/>
        <stop offset="1" stop-color="#2a58b8"/>
      </linearGradient>
    </defs>
    <path d="M0 420 C40 300 150 190 280 60 C330 10 420 20 500 40 C620 70 690 180 660 330 C640 470 560 560 470 620 L362 790 L362 820 L0 820 Z" fill="url(#photoTone)"/>
  </svg>

  <div class="icon-stack">
    <svg class="icon" viewBox="0 0 144 144" role="img" aria-label="Corded ear plugs icon">
      <circle cx="72" cy="72" r="69" fill="var(--white)" stroke="var(--orange)" stroke-width="5"/>
      <circle cx="72" cy="72" r="63" fill="var(--black)"/>
      <g fill="none" stroke="var(--white)" stroke-width="3" stroke-linecap="round">
        <ellipse cx="72" cy="52" rx="34" ry="26"/>
        <path d="M50 72 L96 96 M94 72 L48 96"/>
        <path d="M28 100 q8 -12 20 -6 l-4 12 q-12 6 -16 -6 z"/>
        <path d="M116 100 q-8 -12 -20 -6 l4 12 q12 6 16 -6 z"/>
      </g>
    </svg>
    <svg class="icon" viewBox="0 0 144 144" role="img" aria-label="Earmuffs icon">
      <circle cx="72" cy="72" r="69" fill="var(--white)" stroke="var(--orange)" stroke-width="5"/>
      <circle cx="72" cy="72" r="63" fill="var(--black)"/>
      <g fill="none" stroke="var(--white)" stroke-width="3.5" stroke-linejoin="round">
        <path d="M36 82 C36 40 108 40 108 82"/>
        <path d="M44 80 C44 50 100 50 100 80"/>
        <rect x="30" y="78" width="20" height="36" rx="9"/>
        <rect x="94" y="78" width="20" height="36" rx="9"/>
      </g>
    </svg>
    <svg class="icon" viewBox="0 0 144 144" role="img" aria-label="Ear plug next to ear icon">
      <circle cx="72" cy="72" r="69" fill="var(--white)" stroke="var(--orange)" stroke-width="5"/>
      <circle cx="72" cy="72" r="63" fill="var(--black)"/>
      <g fill="none" stroke="var(--white)" stroke-width="3.5" stroke-linecap="round" stroke-linejoin="round">
        <path d="M26 66 L44 62 L44 82 L26 78 Z"/>
        <path d="M48 72 L56 72"/>
        <path d="M68 62 C68 40 108 36 110 62 C112 80 96 86 96 100 C96 114 80 114 78 104"/>
        <path d="M80 64 C80 52 98 52 98 64 C98 74 88 74 88 84"/>
      </g>
    </svg>
  </div>

  <div class="brand">
    <p class="brand__name"><i class="brand__mark"></i><span>CUTWRIGHT<br>SUPPLY</span></p>
    <p class="brand__tagline">Precision cutting gear for every workshop</p>
    <p class="brand__url">www.cutwrightsupply.com</p>
  </div>

  <div class="hazard-band hazard-band--bottom"></div>
</main>
</body>
</html>
```